Aviation security consulting company needs a website

We need a website design for Brisk Holloway, and aviation security consulting company. Brisk Holloway (www.briskholloway.example) is an aviation security consulting company that works with government and industry stakeholders in over 60 countries on aviation security strategy, governance, and oversight at the regulatory and operational level.
Brisk Holloway is strongly internationally focused.
The website required should be simple, corporate, serious, and communicate professionalism, reliability and honesty. We are trying to give the company a feeling of being well established.
The attached files include the company logo, along with examples of company web page styles that we like.
The Brisk Holloway website need only be around five pages long (landing page, who we are, our services, our clients, contact), though don't feel limited to only five pages.
The existing website (www.briskholloway.example) was rushed and put together using Wix. We don't love the existing website as it looks too amateur, so don't use it as a template.
There is no requirement for any online sales tools to be included in the site. The site is purely informational, with the option of people making contact via email.

```html
<!DOCTYPE html>
<html lang="en">
<head>
<meta charset="utf-8">
<title>Our Services — Brisk Holloway</title>
<link rel="stylesheet" href="https://fonts.googleapis.com/css2?family=Raleway:wght@400;500;600;700&display=swap">
<style>
  :root {
    --navy: #1b2d66;
    --ink: #111111;
    --white: #ffffff;
    --band: #1c1c1c;
    --panel: rgba(255, 255, 255, 0.9);
    --muted: #222222;
  }
  * { box-sizing: border-box; margin: 0; padding: 0; }
  html, body { width: 1200px; height: 952px; overflow: hidden; }
  body {
    position: relative;
    font-family: "Raleway", Arial, sans-serif;
    color: var(--ink);
    background: var(--white);
  }
  .site-header {
    position: absolute; left: 0; top: 0; width: 1200px; height: 95px;
    background: var(--white);
  }
  .brand {
    position: absolute; left: 95px; top: 14px; height: 66px;
    display: flex; align-items: center; gap: 12px;
    text-decoration: none;
  }
  .brand-mark { width: 66px; height: 66px; background: var(--navy); display: block; }
  .brand-name {
    font-size: 34px; font-weight: 700; color: var(--navy); letter-spacing: -0.5px;
  }
  .main-nav { position: absolute; right: 80px; top: 0; height: 70px; display: flex; }
  .main-nav a {
    display: flex; align-items: center; height: 70px; padding: 0 14px;
    font-size: 15px; font-weight: 500; color: var(--ink); text-decoration: none;
    padding-top: 26px; align-items: flex-start;
  }
  .main-nav a.is-active { background: var(--navy); color: var(--white); }

  .hero-band {
    position: absolute; left: 0; top: 95px; width: 1200px; height: 116px;
    background: linear-gradient(90deg, #2a2a2a 0%, #141414 30%, #111 70%, #2c2c2c 100%);
    display: flex; align-items: center; justify-content: center;
  }
  .hero-band p {
    width: 720px; text-align: center; color: #f2f2f2;
    font-size: 18.5px; line-height: 22px; font-weight: 400;
  }
  .cabin-photo {
    position: absolute; left: 0; top: 211px; width: 1200px; height: 687px;
    background:
      radial-gradient(ellipse 260px 420px at 600px 300px, #f4f4f4 0%, #d8d8d8 45%, rgba(120,120,120,0) 100%),
      linear-gradient(90deg, #3d3d3d 0%, #8a8a8a 12%, #b9b9b9 35%, #c9c9c9 50%, #b5b5b5 65%, #858585 88%, #3a3a3a 100%);
  }
  .service-panel {
    position: absolute; top: 222px; width: 494px; height: 654px;
    background: var(--panel);
  }
  .service-panel--left { left: 99px; }
  .service-panel--right { left: 607px; }

  .service { position: absolute; width: 410px; }
  .service h2 {
    font-size: 20px; font-weight: 700; color: var(--navy); line-height: 24px; margin-bottom: 4px;
  }
  .service p, .service li {
    font-size: 12.6px; line-height: 15.5px; color: var(--muted);
  }
  .service ul { list-style: none; margin-top: 14px; padding-left: 14px; }
  .service li { position: relative; padding-left: 19px; }
  .service li::before {
    content: ""; position: absolute; left: 0; top: 5px;
    border-left: 5px solid var(--ink); border-top: 3px solid transparent; border-bottom: 3px solid transparent;
  }

  .site-footer {
    position: absolute; left: 0; top: 898px; width: 1200px; height: 54px;
    background: var(--white); font-size: 11px; color: var(--ink);
  }
  .copyright { position: absolute; left: 96px; top: 21px; }
  .legal-links { position: absolute; right: 94px; top: 20px; }
  .legal-links a { color: var(--ink); text-decoration: none; }
  .legal-links span { margin: 0 6px; }
</style>
</head>
<body>
  <header class="site-header">
    <a class="brand" href="#">
      <span class="brand-mark"></span>
      <span class="brand-name">Brisk Holloway</span>
    </a>
    <nav class="main-nav">
      <a href="#">Home</a>
      <a href="#">Who We Are</a>
      <a href="#" class="is-active">Our Services</a>
      <a href="#">Our Clients</a>
      <a href="#">Contact</a>
    </nav>
  </header>

  <section class="hero-band">
    <p>In depth knowledge built through years of experience brings the ability to deliver expertise to all areas of aviation security for industry and government stakeholders.</p>
  </section>

  <div class="cabin-photo" role="img" aria-label="Photograph of an empty aircraft cabin aisle between rows of seats"></div>

  <main>
    <div class="service-panel service-panel--left">
      <article class="service" style="left:30px; top:40px;">
        <h2>Civil Aviation Authority / Regulator</h2>
        <p>Aviation security regulatory agencies are required to navigate a plethora of conflicting domestic regulation, along with regional and international aviation security requirements.<br>In addition, civil aviation authorities are required to ensure these regulations are appropriately implemented at the national level. Brisk Holloway can assist by, inter alia, developing regulation and other regulatory mechanisms, training national inspectors, and developing audit and compliance assessment tools and programs.</p>
      </article>
      <article class="service" style="left:30px; top:259px;">
        <h2>Air Cargo / Handling Agent</h2>
        <p>Air cargo security is seeing rapid changes, with issues such as pre-loading advanced cargo information, electronic consignment security declarations, and secure supply chains becoming more important. Regulators continue to move away from 100% screening at airports towards whole of supply chain approaches incorporating more industry stakeholders.<br>Brisk Holloway can assist air cargo operators meet aviation security obligations while ensuring facilitation and profitability are maintained.</p>
      </article>
      <article class="service" style="left:30px; top:466px;">
        <h2>Airline</h2>
        <p>Brisk Holloway can work with airlines on security issues such as security program development, station inspection and audit, strategic guidance, and change management.</p>
      </article>
    </div>

    <div class="service-panel service-panel--right">
      <article class="service" style="left:41px; top:42px;">
        <h2>Airport Operations and Screening</h2>
        <p>Brisk Holloway can work with airports and airport designers to ensure security is incorporated in airport designs, and is maximised within existing airport environments. Services include:</p>
        <ul>
          <li>Passenger screening point design and efficiency</li>
          <li>audit and inspection of processes</li>
          <li>access and egress</li>
          <li>airport security management</li>
          <li>vulnerability assessments (including front of house design)</li>
        </ul>
      </article>
      <article class="service" style="left:42px; top:259px;">
        <h2>Capacity Development</h2>
        <p>Every country is different, and while States must meet the same international standards, there is no 'one size fits all' approach. Each State must develop solutions that are sustainable in their economies.<br>Brisk Holloway has extensive experience working in partnership with developing economies to implement incremental changes to aviation security that don't just meet immediate needs, but maintain their viability over the medium and long term.</p>
      </article>
      <article class="service" style="left:44px; top:454px;">
        <h2>Training</h2>
        <p>Brisk Holloway has experienced aviation security trainers who can take participants through course material prepared by your organisation, or can develop training material tailored to your requirements.</p>
      </article>
    </div>
  </main>

  <footer class="site-footer">
    <p class="copyright">© 2016. Brisk Holloway. All Rights Reserved.</p>
    <p class="legal-links"><a href="#">Terms</a><span>|</span><a href="#">Privacy Policy</a></p>
  </footer>
</body>
</html>
```